Rebrand our dated accomodation business website "Tallowind Quay Residences"

we have a wordpress website ( www.tallowindquay.com.au) that is old and out dated .
I will need a new updated SQUARESPACE website (in which i already have ) with a fresh new design , also new logo and an easy site to manage from my end.
Need to connect our socials - facebook and instagram and our new site
Check out "brindle cove landing" for inspiration...
These apartments are consists of -
-One bedroom One bath
-Two bedroom One bath
-Two bedroom Two bath
-Three bedroom Two bath
all other information is on our current website
KEEP it simple and fresh
ALSO WE DONT HAVE HUGE BIG BOATS IN THE MARINA SO PLEASE DONT HAVE THAT IN THE LOGO

Target Market(s)

Anyone looking for accomodation !! we have 64 rooms !!

Industry/Entity Type

accomodation / short stays

Coding

Coded - Design and coding required

Number of Pages Required

5+ page

Requirements
Must have
• Fresh , modern and easy to use.....have a hoilday vibe , also use natural colours
Nice to have
• i like accomodation website like ....https://fernandgrove.com.au/luxury-coastal-accommodation/ or https://theorvellainn.com/
Should not have
• please do not use bright colours and scripted fonts

```html
<!DOCTYPE html>
<html lang="en">
<head>
<meta charset="utf-8">
<title>Tallowind Quay Residences</title>
<link href="https://fonts.googleapis.com/css2?family=Poppins:wght@300;400;500;600;700&display=swap" rel="stylesheet">
<style>
:root{
  --teal:#1f7a97;
  --teal-dark:#1a6a83;
  --ink:#1f2326;
  --muted:#4a5055;
  --mist:#f1f6f6;
  --white:#ffffff;
  --line:#d9e2e4;
}
*{box-sizing:border-box;margin:0;padding:0}
html,body{width:1200px;height:4234px;overflow:hidden}
body{font-family:'Poppins',sans-serif;color:var(--ink);background:var(--white);position:relative}
a{color:inherit;text-decoration:none}
.abs{position:absolute}

/* Hero */
.hero{position:absolute;left:0;top:0;width:1200px;height:625px;
  background:linear-gradient(90deg,rgba(20,40,55,.55) 0%,rgba(20,40,55,.2) 55%,rgba(20,40,55,0) 100%),
  linear-gradient(180deg,#3d5a78 0%,#7c97b2 30%,#8b8f85 55%,#4f6b3a 75%,#a58d6a 100%)}
.brand{font-family:'Poppins',sans-serif;font-weight:500;font-size:30px;letter-spacing:.5px;color:var(--teal);display:flex;align-items:center;gap:10px}
.brand .dot{width:12px;height:12px;border-radius:50%;background:var(--teal)}
.hero .brand{left:107px;top:22px;color:#2a8fb0}
.nav{left:452px;top:33px;display:flex;gap:23px;font-size:11.5px;color:#fff}
.nav-cta{left:967px;top:30px;width:128px;height:24px;background:var(--teal);color:#fff;font-size:11px;display:flex;align-items:center;justify-content:center}
.hero-kicker{left:109px;top:162px;color:#fff;font-size:18px;font-weight:400}
.hero-title{left:107px;top:196px;color:#fff;font-size:46px;font-weight:700;line-height:52px}
.hero-text{left:107px;top:322px;width:560px;color:#fff;font-size:17px;font-weight:600;line-height:32px}
.btn{display:flex;align-items:center;justify-content:center;font-size:11.5px}
.hero-btn{left:107px;top:442px;width:207px;height:48px;background:var(--teal-dark);color:#fff}

/* Intro */
.kicker{font-size:10.5px;color:var(--teal);text-transform:uppercase;letter-spacing:.3px}
.center{left:0;width:1200px;text-align:center}
.h2{font-size:33px;font-weight:400;color:var(--ink);line-height:42px}
.lead{font-size:11.5px;line-height:21px;color:var(--muted)}

/* Apartments */
.suites{position:absolute;left:0;top:852px;width:1200px;height:1351px;background:var(--mist)}
.split{left:497px;top:83px;width:14px;height:90px}
.card{position:absolute;width:464px}
.card .photo{width:464px;height:401px}
.card .row{display:flex;justify-content:space-between;align-items:baseline;margin-top:22px;padding:0 2px}
.card h3{font-size:21px;font-weight:400}
.card .sleeps{font-size:11px;color:var(--teal)}
.card p{font-size:11.5px;line-height:21px;color:var(--muted);margin-top:6px;padding:0 2px;width:455px}
.card .more{display:inline-block;margin:7px 2px 0;font-size:11.5px;color:var(--teal);border-bottom:1px solid var(--teal);line-height:16px}

/* Amenities */
.amen-photo{left:0;top:2277px;width:690px;height:611px;background:linear-gradient(160deg,#eef1f2 0%,#dfe4e6 45%,#c9cfd1 70%,#7f8c94 100%)}
.amen-card{left:598px;top:2349px;width:497px;height:462px;background:#fff;box-shadow:0 6px 24px rgba(0,0,0,.1);padding:66px 36px 0}
.amen-card .h2{font-size:31px;line-height:41px;margin-top:8px}
.amen-card .lead{margin-top:22px;width:420px}
.amen-list{display:grid;grid-template-columns:204px 200px;row-gap:14px;margin-top:18px}
.amen{display:flex;align-items:center;gap:15px;font-size:11.5px;color:var(--muted)}
.ico{width:33px;height:30px;border-radius:5px;background:var(--teal);display:flex;align-items:center;justify-content:center}

/* Coast */
.video{left:107px;top:3094px;width:988px;height:485px;background:radial-gradient(ellipse at 50% 40%,#6f7d6a 0%,#5a6b5e 30%,#3aa0a5 55%,#1a5c74 80%,#0f4660 100%)}
.play{left:571px;top:3306px;width:60px;height:60px}

/* CTA */
.cta{position:absolute;left:0;top:3643px;width:1200px;height:342px;background:var(--teal)}
.cta .kicker{color:#fff}
.cta-title{font-size:31px;font-weight:400;color:#fff;letter-spacing:.5px}
.cta-btn{left:496px;top:204px;width:208px;height:48px;background:#fff;color:var(--teal)}
.cta-art{left:888px;top:138px;width:279px;height:181px;background:linear-gradient(135deg,rgba(255,255,255,.12),rgba(255,255,255,.03))}

/* Footer */
.footer .brand{left:103px;top:4040px;font-size:30px}
.foot-text{left:107px;top:4082px;width:400px;font-size:11.5px;line-height:21px;color:var(--muted)}
.foot-col{font-size:11.5px;line-height:20px;color:var(--muted)}
.foot-col h4{font-size:11.5px;font-weight:600;color:var(--ink);margin-bottom:15px}
.foot-col .ci{display:flex;align-items:center;gap:10px}
.divider{left:107px;top:4171px;width:988px;height:1px;background:var(--line)}
.copy{font-size:11px;color:var(--muted)}
</style>
</head>
<body>

<header class="hero" role="img" aria-label="Apartment building with balconies and gardens beside a pathway">
</header>
<div class="abs brand" style="left:107px;top:20px;color:#2a8fb0"><span>Tallowind Quay</span></div>
<nav class="abs nav"><a>Home</a><a>About Us</a><a>ACCommodation</a><a>Our Location</a><a>New/Events</a><a>Contact Us</a></nav>
<a class="abs btn nav-cta">Book Direct &amp; Save!</a>
<p class="abs hero-kicker">Coastal stays on the water</p>
<h1 class="abs hero-title">Slow mornings. Salt air.<br>A stay by the marina.</h1>
<p class="abs hero-text">Settle into light-filled apartment living beside the harbour, where calm interiors and open water create an effortless coastal escape.</p>
<a class="abs btn hero-btn">Discover the apartments</a>

<section>
  <p class="abs center kicker" style="top:687px">A quieter kind of getaway</p>
  <h2 class="abs center h2" style="top:708px">Designed For Easy Days By The Water.</h2>
  <p class="abs center lead" style="top:761px;left:310px;width:580px">Tallowind Quay Residences brings together contemporary comfort, generous space, and the relaxed rhythm of the coast — all just moments from the waterfront.</p>
</section>

<section class="suites">
  <p class="abs kicker" style="left:106px;top:68px">Stay awhile</p>
  <h2 class="abs h2" style="left:106px;top:88px;font-size:32px">Apartments For Every<br>Pace Of Travel.</h2>
  <svg class="abs split" viewBox="0 0 14 90"><path d="M1 0V32L10 45L1 58V90" fill="none" stroke="#8a9499" stroke-width="1"/></svg>
  <p class="abs lead" style="left:538px;top:99px;width:540px">Tallowind Quay Residences brings together contemporary comfort, generous space, and the relaxed rhythm of the coast — all just moments from the waterfront.</p>

  <article class="card" style="left:107px;top:195px">
    <div class="photo" role="img" aria-label="Bedroom with king bed, navy throw and beach artwork" style="background:linear-gradient(180deg,#e9eaea 0%,#d8dad9 50%,#2b3b58 75%,#e4e6e8 100%)"></div>
    <div class="row"><h3>One Bedroom Apartment</h3><span class="sleeps">Sleeps 2</span></div>
    <p>A peaceful hideaway with soft natural textures, a king bedroom, and a private balcony for slow mornings.</p>
    <a class="more">Explore suite</a>
  </article>
  <article class="card" style="left:630px;top:195px">
    <div class="photo" role="img" aria-label="Twin bedroom with striped cushions and navy bedding" style="background:linear-gradient(180deg,#e7e8e6 0%,#d3d5d2 45%,#243654 70%,#d7d9da 100%)"></div>
    <div class="row"><h3>Two Bedroom Apartment</h3><span class="sleeps">Sleeps 2</span></div>
    <p>Open-plan living, generous lounge spaces, and a relaxed coastal palette made for shared escapes.</p>
    <a class="more">Explore suite</a>
  </article>
  <article class="card" style="left:107px;top:767px">
    <div class="photo" role="img" aria-label="Bedroom with white linen, green cushions and leaf artwork" style="background:linear-gradient(180deg,#dfe3e6 0%,#d1d6d8 45%,#f0f1f1 70%,#5b4a40 100%)"></div>
    <div class="row"><h3>Two Bedroom, Two Bathroom</h3><span class="sleeps">Sleeps 4</span></div>
    <p>A little more room to unwind, with two serene bedrooms, two bathrooms, and sweeping water views.</p>
    <a class="more">Explore suite</a>
  </article>
  <article class="card" style="left:630px;top:767px">
    <div class="photo" role="img" aria-label="Bright white kitchen with stainless appliances" style="background:linear-gradient(180deg,#e8e9e9 0%,#cfd2d3 50%,#b9bcbd 75%,#e3e4e4 100%)"></div>
    <div class="row"><h3>Three Bedroom Apartment</h3><span class="sleeps">Sleeps 2</span></div>
    <p>Our most spacious stay, designed for families and friends with generous living and dining spaces</p>
    <a class="more">Explore suite</a>
  </article>
</section>

<section>
  <div class="abs amen-photo" role="img" aria-label="Light living room with rattan pendant lamp and white dining table"></div>
  <div class="abs amen-card">
    <p class="kicker">For slow afternoons</p>
    <h2 class="h2">Everything You Need,<br>Nothing You Don’t.</h2>
    <p class="lead">Spend the day between the pool, the marina, and the shoreline. Here, the essentials are considered and the pace is entirely your own.</p>
    <div class="amen-list">
      <div class="amen"><span class="ico"><svg width="18" height="14" viewBox="0 0 18 14" fill="none" stroke="#fff" stroke-width="1.4"><path d="M1 10c2-2 4 2 6 0s4 2 6 0 3 1 4 0M1 13c2-2 4 2 6 0s4 2 6 0 3 1 4 0M5 8V1M12 8V1M5 4h7"/></svg></span>Resort-style pool</div>
      <div class="amen"><span class="ico"><svg width="18" height="16" viewBox="0 0 18 16" fill="none" stroke="#fff" stroke-width="1.4"><circle cx="9" cy="6" r="3.5"/><path d="M9 1V0M3 6H2M16 6h-1M1 14h16"/></svg></span>Sun Terrace</div>
      <div class="amen"><span class="ico"><svg width="16" height="18" viewBox="0 0 16 18" fill="none" stroke="#fff" stroke-width="1.4"><circle cx="8" cy="3" r="2"/><path d="M8 5v12M4 8h8M1 11c0 4 4 6 7 6s7-2 7-6"/></svg></span>Marina Frontage</div>
      <div class="amen"><span class="ico"><svg width="18" height="16" viewBox="0 0 18 16" fill="none" stroke="#fff" stroke-width="1.4"><path d="M2 6h11v4a4 4 0 0 1-4 4H6a4 4 0 0 1-4-4zM13 7h2a2 2 0 0 1 0 4h-2M6 1v3M9 1v3"/></svg></span>Cafés Nearby</div>
      <div class="amen"><span class="ico"><svg width="18" height="14" viewBox="0 0 18 14" fill="none" stroke="#fff" stroke-width="1.4"><path d="M1 5a11 11 0 0 1 16 0M4 8a7 7 0 0 1 10 0M7 11a3 3 0 0 1 4 0"/><circle cx="9" cy="13" r=".6" fill="#fff"/></svg></span>Complimentary Wi-Fi</div>
      <div class="amen"><span class="ico"><svg width="16" height="18" viewBox="0 0 16 18" fill="none" stroke="#fff" stroke-width="1.4"><rect x="1" y="1" width="14" height="16" rx="2"/><path d="M5 14V4h4a3 3 0 0 1 0 6H5"/></svg></span>Secure Parking</div>
    </div>
  </div>
</section>

<section>
  <p class="abs center kicker" style="top:2955px">By the harbour</p>
  <h2 class="abs center h2" style="top:2978px">Close To The Coast, Connected To Everything.</h2>
  <p class="abs center lead" style="top:3031px;left:310px;width:580px">Wake to marina views, wander to the beach, and spend your evenings exploring local dining, coastal walks, and the easy charm of the foreshore.</p>
  <div class="abs video" role="img" aria-label="Aerial view of a rocky headland surrounded by turquoise surf"></div>
  <svg class="abs play" viewBox="0 0 60 60"><circle cx="30" cy="30" r="29" fill="#fff" fill-opacity=".85"/><path d="M25 20l14 10-14 10z" fill="#3b4750"/></svg>
</section>

<section class="cta">
  <p class="abs center kicker" style="top:95px">Your coast escape awaits</p>
  <h2 class="abs center cta-title" style="top:116px">STAY WHERE THE WATER SETS THE PACE.</h2>
  <p class="abs center" style="top:161px;font-size:11.5px;color:#fff">Plan your next waterfront stay and discover the quiet beauty of Tallowind Quay Residences.</p>
  <a class="abs btn cta-btn">Discover the apartments</a>
  <div class="abs cta-art" role="img" aria-label="Line drawing of a modern apartment building"></div>
</section>

<footer class="footer">
  <div class="abs brand"><span>Tallowind Quay</span></div>
  <p class="abs foot-text">Relaxed waterfront apartment stays designed for bright mornings, easy days, and memorable coastal escapes.</p>
  <div class="abs foot-col" style="left:598px;top:4036px">
    <h4>Explore</h4>
    <p>Apartments</p><p>Amenities</p><p>Location</p>
  </div>
  <div class="abs foot-col" style="left:789px;top:4036px">
    <h4>Contact</h4>
    <p class="ci"><svg width="11" height="13" viewBox="0 0 11 13"><path d="M5.5 0A5 5 0 0 0 .5 5c0 4 5 8 5 8s5-4 5-8a5 5 0 0 0-5-5z" fill="#1f7a97"/><circle cx="5.5" cy="5" r="1.8" fill="#fff"/></svg>14 Harbourview Lane, Tallowind</p>
    <p class="ci"><svg width="11" height="9" viewBox="0 0 11 9"><rect width="11" height="9" rx="1" fill="#1f7a97"/><path d="M0 1l5.5 4L11 1" stroke="#fff" fill="none"/></svg>stay@tallowindquay.com</p>
    <p class="ci"><svg width="11" height="11" viewBox="0 0 11 11"><path d="M2 0l2 2.5-1 1.5a7 7 0 0 0 4 4l1.5-1L11 9l-1.5 2C5 11 0 6 0 1.5z" fill="#1f7a97"/></svg>+61 2 5550 1234</p>
  </div>
  <div class="abs divider"></div>
  <p class="abs center copy" style="top:4191px">© 2026 Tallowind Quay Residences</p>
</footer>

</body>
</html>
```